Hair and Beauty wholesaler Monthly Sales/Specials Flyer for the month of June

Project Scope
Company title: Kestrel Hair Nail and Beauty Supplies
Project scope: Monthly Sales/Specials Flyer for the month of June
Flyer size: A4 1 sided page
Used for: Version 1 – print ready pdf with trim/bleed marks (.pdf). Versions 2 – EDM - Same as version 1 but saved a (.jpg)

Demographics
Buyer/Intended audience: Hair & Beauty Salons (whole sale pricing)

Objective
Main objective: Sell products to salons at wholesale pricing – Good bargain deals

Style, Tone and Image
Appear professional, bright, bargains, Good deals, colours used on flyer must link in with red and white company logo

Flyer Header:
Kestrel Hair Nail and Beauty Supplies Logo
Kestrel Hair Nail and Beauty Supplies
Serving the City of Sydney
Suite 4, Level 3, The Farrowden Building, 617 Tillman Street, Sydney NSW 2000
T 02 9584 7302 W kestrelsalonstock.com.au

Flyer Title: Mighty Midyear Specials
Valid for the Month of June only. Don’t miss out!

Deal 1:
Header: Salon Fair Deal
Sub header: Vorn8 Sets - Limited Edition - 3 Scissors & 1 Holster - Only $89.95
Small text at the footer of deal:
Offer Includes: 1 x Vorn8 Scissor 5”, 1 x Vorn8 Scissor 6”, 1 x Vorn8 Thinning Scissor 6”, 1 x Scissor Holster
Image: Please show image of 2 scissors, 1 thinning scissor, scissor holster

Deal 2:
Header: Peltra Marigel Hot Wax 1Kg
Normally $27.95
Now only $19.95
Total Savings $8
Image: Peltra Marigel Hot Wax 1Kg

Deal 3:
Header: Osvane Lumique & Nurtiva Litre Deal
Buy 2 for only $50
Total savings $23.90
Image: 1 Osvane Lumique Litre Bottle and 1 Osvane Nurtiva Litre Bottle
Small text at the footer of deal: Valid on Osvane Lumique and Osvane Nurtiva 1L Shampoo and Conditioner.

Deal 4:
Header: Charcoal Peel Off Mask 3 pack
Intro price
Only $8.95
Image: Charcoal Peel Off Mask

Deal 5:
Header: Buy 7 Bronzi Milano Hair Colour Get Free Flarelite Blue Dust Free Bleach 500g
Total savings $9.95
Small text at the footer of deal: Maximum 2 free bleach per customer
Image: 7 Bronzi Milano Hair Colour + 1 Flarelite Blue Dust Free Bleach

Deal 6: Ketch Ripple Edge 4000 Combo
Only $119.95
Total Savings $70
Image: 1 Ketch Ripple super edge 4000 clipper, 1 Ketch Ripple super edge 4000 trimmer

Flyer footer:
Small text: Not to be used in conjunction with any other discounts/offers. Valid until 30 June 2017 or while stocks last.

Target Market(s)

Hair and Beauty Salons

Industry/Entity Type

Hair And Beauty

Colors

Designer to choose colors to be used in the design.

Requirements
Must have
• colours used on flyer must link in with red and white company logo
• must use the images provided in brief
• 1 sided A4 page
Nice to have
• Appear professional, bright, bargains, Good deals,
Should not have
• comedy

```html
<!DOCTYPE html>
<html lang="en">
<head>
<meta charset="utf-8">
<title>Kestrel Hair Nail and Beauty Supplies – June Specials</title>
<link href="https://fonts.googleapis.com/css2?family=Roboto+Condensed:wght@400;700&family=Open+Sans:wght@400;600;700&display=swap" rel="stylesheet">
<style>
  :root {
    --red: #e3202b;
    --red-dark: #c4121c;
    --ink: #2b2b2b;
    --band: #3e3e3e;
    --grey-light: #ececec;
    --grey-mid: #c9c9c9;
    --backdrop: #efece8;
    --white: #ffffff;
  }
  * { box-sizing: border-box; margin: 0; padding: 0; }
  html, body { width: 1200px; height: 850px; overflow: hidden; background: var(--backdrop); }
  .stage { position: relative; width: 1200px; height: 850px; }
  .page {
    position: absolute; top: 52px; height: 748px; overflow: hidden;
    background: var(--white); box-shadow: 0 3px 10px rgba(0,0,0,.25);
    font-family: "Open Sans", Arial, sans-serif;
  }
  .page--front { left: 57px; width: 528px; }
  .page--back { left: 615px; width: 532px; }
  .page svg.art { position: absolute; inset: 0; }

  .brand { position: absolute; display: flex; align-items: center; gap: 8px; }
  .brand__dot { width: 56px; height: 56px; border-radius: 50%; background: var(--red); flex: none; }
  .brand__name { font-family: "Roboto Condensed", Arial, sans-serif; font-weight: 700; color: var(--red); font-size: 40px; line-height: 1; }
  .brand__tag { font-family: "Roboto Condensed", Arial, sans-serif; font-weight: 700; color: var(--ink); font-size: 11px; margin-top: 3px; }
  .page--front .brand { left: 25px; top: 26px; }
  .page--back .brand { left: 58px; top: 16px; }
  .page--back .brand__dot { width: 46px; height: 46px; }
  .page--back .brand__name { font-size: 34px; }
  .page--back .brand__tag { font-size: 9px; }

  .badge-text {
    position: absolute; left: 43px; top: 204px; width: 100px; text-align: center;
    font-family: "Roboto Condensed", Arial, sans-serif; font-weight: 700; color: var(--white);
    font-size: 18px; line-height: 22px; text-transform: uppercase;
  }

  .headline { position: absolute; left: 30px; top: 404px; font-family: "Roboto Condensed", Arial, sans-serif; }
  .headline__company { color: var(--red); font-weight: 700; font-size: 32px; line-height: 38px; }
  .headline__company span { display: block; }
  .headline__company span:first-child { padding-left: 10px; }
  .headline__sub { font-family: "Open Sans", Arial, sans-serif; color: var(--ink); font-size: 18px; margin-top: 8px; }
  .headline__cta { color: var(--ink); font-weight: 700; font-size: 31px; line-height: 38px; margin-top: 14px; }

  .validity {
    position: absolute; left: 314px; top: 596px; width: 187px; height: 52px; border-radius: 8px;
    background: linear-gradient(#f4f4f4, #b9b9b9); box-shadow: 0 1px 3px rgba(0,0,0,.35);
    font-family: "Roboto Condensed", Arial, sans-serif; font-weight: 700; color: var(--red);
    font-size: 17px; line-height: 21px; text-align: center; padding-top: 5px;
  }

  .contact { position: absolute; left: 34px; top: 696px; color: var(--white); }
  .contact__phone { font-family: "Roboto Condensed", Arial, sans-serif; font-weight: 700; font-size: 19px; }
  .contact__web { display: flex; align-items: center; gap: 6px; font-size: 15px; margin-top: 2px; }
  .address { position: absolute; left: 328px; top: 700px; color: var(--white); font-size: 8.5px; line-height: 12px; font-style: normal; }
  .address__line { display: flex; gap: 4px; align-items: center; }
  .address__line--indent { padding-left: 13px; }

  .deal { position: absolute; left: 201px; width: 232px; color: var(--white); font-size: 9px; line-height: 12px; white-space: nowrap; }
  .deal__title { color: var(--red); font-weight: 700; }

  .back-footer {
    position: absolute; left: 0; right: 0; bottom: 10px; display: flex; justify-content: center; align-items: center; gap: 6px;
    color: var(--white); font-size: 14px;
  }
</style>
</head>
<body>
<div class="stage">

  <!-- Front page -->
  <section class="page page--front">
    <svg class="art" width="528" height="748" viewBox="0 0 528 748">
      <defs>
        <linearGradient id="frontTop" x1="0" y1="0" x2="1" y2="0">
          <stop offset="0" stop-color="#f2f2f2"/>
          <stop offset="1" stop-color="#bdbdbd"/>
        </linearGradient>
        <linearGradient id="portrait" x1="0" y1="0" x2="1" y2="1">
          <stop offset="0" stop-color="#cfc9c3"/>
          <stop offset=".5" stop-color="#e2c39c"/>
          <stop offset="1" stop-color="#e5b9a0"/>
        </linearGradient>
        <linearGradient id="redBand" x1="0" y1="0" x2="1" y2="0">
          <stop offset="0" stop-color="#ef3d47"/>
          <stop offset="1" stop-color="#d8141f"/>
        </linearGradient>
      </defs>
      <rect width="528" height="460" fill="url(#frontTop)"/>
      <g role="img" aria-label="Photo of a smiling woman with long wavy blonde hair">
        <rect x="250" y="0" width="278" height="460" fill="url(#portrait)"/>
      </g>
      <path d="M0 0 H528 V40 C380 60 260 110 170 125 C100 135 40 125 0 110 Z" fill="#f6f6f6"/>
      <path d="M0 112 C60 128 120 136 180 124 C280 104 400 55 528 42" fill="none" stroke="var(--red)" stroke-width="3"/>
      <path d="M0 370 C120 330 260 320 380 360 C440 380 490 420 528 452 V748 H0 Z" fill="url(#redBand)"/>
      <path d="M0 400 C120 355 260 350 380 385 C440 403 490 440 528 462 V748 H0 Z" fill="var(--white)"/>
      <g transform="translate(93 238)">
        <rect x="-50" y="-50" width="100" height="100" fill="var(--red)"/>
        <rect x="-50" y="-50" width="100" height="100" fill="var(--red)" transform="rotate(22.5)"/>
        <rect x="-50" y="-50" width="100" height="100" fill="var(--red)" transform="rotate(45)"/>
        <rect x="-50" y="-50" width="100" height="100" fill="var(--red)" transform="rotate(67.5)"/>
        <circle r="52" fill="var(--red-dark)" stroke="var(--white)" stroke-width="2"/>
      </g>
      <path d="M0 680 C160 650 360 655 528 685 V748 H0 Z" fill="url(#redBand)"/>
      <path d="M0 672 C160 642 360 647 528 677" fill="none" stroke="var(--red)" stroke-width="2"/>
    </svg>

    <div class="brand">
      <div class="brand__dot"></div>
      <div>
        <div class="brand__name">Kestrel</div>
        <div class="brand__tag">Hair, Nail and Beauty Supplies</div>
      </div>
    </div>

    <div class="badge-text">Mighty Midyear Specials</div>

    <div class="headline">
      <h1 class="headline__company"><span>Kestrel Hair Nail</span><span>and Beauty Supplies</span></h1>
      <p class="headline__sub">Monthly Specials Flyer for the month of June</p>
      <p class="headline__cta">Valid for the Month of June only<br>Don’t miss out!</p>
    </div>

    <div class="validity">Valid until 30 June 2017<br>or while stocks last</div>

    <div class="contact">
      <div class="contact__phone">CALL US:02 9584 7302</div>
      <div class="contact__web">
        <svg width="14" height="14" viewBox="0 0 14 14" aria-hidden="true"><circle cx="7" cy="7" r="6" fill="none" stroke="#fff" stroke-width="1.3"/><ellipse cx="7" cy="7" rx="2.6" ry="6" fill="none" stroke="#fff" stroke-width="1"/><line x1="1" y1="7" x2="13" y2="7" stroke="#fff"/></svg>
        kestrelsalonstock.com.au
      </div>
    </div>

    <address class="address">
      <div class="address__line">
        <svg width="9" height="11" viewBox="0 0 9 11" aria-hidden="true"><path d="M4.5 0C2 0 0 2 0 4.4 0 7.5 4.5 11 4.5 11S9 7.5 9 4.4C9 2 7 0 4.5 0Z" fill="#fff"/><circle cx="4.5" cy="4.3" r="1.6" fill="var(--red)"/></svg>
        Serving the City of Sydney
      </div>
      <div class="address__line address__line--indent">Suite 4, Level 3, The Farrowden Building,</div>
      <div class="address__line address__line--indent">617 Tillman Street, Sydney NSW 2000</div>
    </address>
  </section>

  <!-- Back page -->
  <section class="page page--back">
    <svg class="art" width="532" height="748" viewBox="0 0 532 748">
      <defs>
        <linearGradient id="backBody" x1="0" y1="0" x2="1" y2="0">
          <stop offset="0" stop-color="#d6d6d6"/>
          <stop offset=".5" stop-color="#f4f4f4"/>
          <stop offset="1" stop-color="#d6d6d6"/>
        </linearGradient>
        <linearGradient id="productTone" x1="0" y1="0" x2="1" y2="1">
          <stop offset="0" stop-color="#e9e9e9"/>
          <stop offset="1" stop-color="#c7c7c7"/>
        </linearGradient>
      </defs>
      <rect width="532" height="748" fill="url(#backBody)"/>
      <path d="M0 0 H532 V42 C400 55 300 95 200 95 C120 95 50 80 0 68 Z" fill="var(--white)"/>
      <path d="M0 70 C60 88 130 100 210 98 C320 95 420 50 532 42" fill="none" stroke="var(--red)" stroke-width="4"/>

      <g fill="var(--band)">
        <polygon points="100,90 432,84 432,182 100,188"/>
        <polygon points="100,188 432,194 432,292 100,286"/>
        <polygon points="100,296 432,290 432,388 100,394"/>
        <polygon points="100,398 432,404 432,502 100,496"/>
        <polygon points="100,504 432,498 432,596 100,602"/>
        <polygon points="100,606 432,612 432,700 100,694"/>
      </g>

      <g stroke="var(--red)" stroke-width="3" fill="var(--white)">
        <polygon points="135,99 170,119 170,159 135,179 100,159 100,119"/>
        <polygon points="395,203 430,223 430,263 395,283 360,263 360,223"/>
        <polygon points="135,305 170,325 170,365 135,385 100,365 100,325"/>
        <polygon points="395,409 430,429 430,469 395,489 360,469 360,429"/>
        <polygon points="135,513 170,533 170,573 135,593 100,573 100,533"/>
        <polygon points="395,612 430,632 430,672 395,692 360,672 360,632"/>
      </g>
      <g role="img" aria-label="Product photo: Vorn8 scissor set with holster"><rect x="112" y="125" width="46" height="28" fill="url(#productTone)"/></g>
      <g role="img" aria-label="Product photo: Peltra Marigel hot wax 1kg tub"><rect x="375" y="228" width="40" height="30" fill="#e98fb4"/></g>
      <g role="img" aria-label="Product photo: Osvane litre shampoo bottle"><rect x="125" y="318" width="20" height="54" fill="#c8202d"/></g>
      <g role="img" aria-label="Product photo: charcoal peel off mask pack"><rect x="380" y="428" width="30" height="42" fill="#4a5560"/></g>
      <g role="img" aria-label="Product photo: Bronzi Milano hair colour tube and box"><rect x="108" y="540" width="54" height="26" fill="#e4e6d6"/></g>
      <g role="img" aria-label="Product photo: Ketch Ripple Edge clipper"><rect x="387" y="626" width="16" height="52" fill="#a9c3c8"/></g>

      <path d="M0 712 C160 700 360 700 532 712 V748 H0 Z" fill="var(--red)"/>
      <path d="M0 704 C160 692 360 692 532 704" fill="none" stroke="var(--red)" stroke-width="2"/>
    </svg>

    <div class="brand">
      <div class="brand__dot"></div>
      <div>
        <div class="brand__name">Kestrel</div>
        <div class="brand__tag">Hair, Nail and Beauty Supplies</div>
      </div>
    </div>

    <div class="deal" style="top:112px">
      <div class="deal__title">Salon Fair Deal</div>
      <div>Vorn8 Sets - Limited Edition - 3 Scissors &amp; 1 Holster</div>
      <div>Only $89.95</div>
      <div>Offer Includes: 1 x Vorn8 Scissor 5”, 1 x Vorn8 Scissor 6”,</div>
      <div>1 x Vorn8 Thinning Scissor 6”, 1 x Scissor Holster</div>
    </div>
    <div class="deal" style="top:216px">
      <div class="deal__title">Peltra Marigel Hot Wax 1Kg</div>
      <div>Normally $27.95</div>
      <div>Now only $19.95</div>
      <div>Total Savings $8</div>
    </div>
    <div class="deal" style="top:316px">
      <div class="deal__title">Osvane Lumique &amp; Nurtiva Litre Deal</div>
      <div>Buy 2 for only $50</div>
      <div>Total savings $23.90</div>
      <div>Valid on Osvane Lumique and Osvane Nurtiva</div>
      <div>1L Shampoo and Conditioner</div>
    </div>
    <div class="deal" style="top:420px">
      <div class="deal__title">Charcoal Peel<br>Off Mask 3 pack</div>
      <div>Intro price</div>
      <div>Only $8.95</div>
    </div>
    <div class="deal" style="top:534px">
      <div class="deal__title">Buy 7 Bronzi Milano Hair Colour<br>Get Free Flarelite Blue Dust Free Bleach 500g</div>
      <div>Total savings $9.95</div>
      <div>Maximum 2 free bleach per customer</div>
    </div>
    <div class="deal" style="top:638px">
      <div class="deal__title">Ketch Ripple Edge 4000 Combo</div>
      <div>Only $119.95</div>
      <div>Total Savings $70</div>
    </div>

    <div class="back-footer">
      <svg width="14" height="14" viewBox="0 0 14 14" aria-hidden="true"><circle cx="7" cy="7" r="6" fill="none" stroke="#fff" stroke-width="1.3"/><ellipse cx="7" cy="7" rx="2.6" ry="6" fill="none" stroke="#fff" stroke-width="1"/><line x1="1" y1="7" x2="13" y2="7" stroke="#fff"/></svg>
      kestrelsalonstock.com.au
    </div>
  </section>

</div>
</body>
</html>
```